Health and Wellness. I am an energetic, but not over the top, Certified Personal Trainer and Nutriti

I need a flyer, 8.5 x 11, representing my company to be displayed in a Doctor's office that specializes in Pain Medicine. Most, if not all, of these clients experience pain or have some chronic diseases such as high blood pressure, high cholesterol, back pain, joint pain, etc. So the flyer should convey that exercise and nutrition reduce/relieves pain and references some of these ailments. Ideally, the flyer should depict an overweight person exercising with a content, or somewhat content or smiling expression on their face in some part of the flyer. My services cover nutrition and include personal training to where I Ideally train people in their home, equipment permitting, or outside in our local Floridian Parks, and sometimes beaches. This flyer will be in a display case, and the bottom right 8.5 x5 cm will need to be blank, or allow for me to input the back of my business car into it, as I'll have business cards readily available in front of the flyer to be taken. I've included some versions of my logos to be added to the flyer. The other picture is of the flyer holder, with business card area, that this flyer will be presented in. Finally, I've attached a pic of what the back of my business card looks like to be input into that bottom right hand corner. You'll be able to see the area in the bottom right that will display my business cards.
Target Market(s)
People looking for weight loss through Nutrition and Fitness. Those looking to relieve joint and/or back pain or those with Chronic diseases such as high blood pressure, high cholesterol, etc.
Industry/Entity Type
Doctor
Requirements
Must have
- Resemble my Logo's color scheme: Red, Teal, and Grey. Some type of photo of an overweight or slightly overweight person exercising.

```html
<!DOCTYPE html>
<html lang="en">
<head>
<meta charset="utf-8">
<title>Brightwell Fitness Flyer</title>
<link rel="stylesheet" href="https://fonts.googleapis.com/css2?family=Bebas+Neue&family=Lato:wght@400;700&family=Raleway:wght@300;600&display=swap">
<style>
  :root {
    --teal: #33b5a5;
    --teal-deep: #22a190;
    --red: #e8454f;
    --grey-bg: #eeeeee;
    --grey-text: #4d4d4d;
    --ink: #262626;
    --white: #ffffff;
    --page: #e4e4e2;
  }
  * { margin: 0; padding: 0; box-sizing: border-box; }
  html, body { width: 1200px; height: 1200px; overflow: hidden; background: var(--page); }
  .flyer {
    position: absolute; left: 160px; top: 30px; width: 880px; height: 1140px;
    background: var(--grey-bg); overflow: hidden;
    box-shadow: 0 4px 18px rgba(0,0,0,.12);
    font-family: "Lato", sans-serif;
  }
  .hero-photo {
    position: absolute; left: 0; top: 0; width: 880px; height: 250px;
    background: linear-gradient(180deg, #3f6b3a 0%, #6f8f55 45%, #8b8a74 80%, #6d6a5e 100%);
  }
  .headline-band {
    position: absolute; left: 0; top: 252px; width: 880px; height: 188px;
    background: var(--teal); color: var(--white); text-align: center;
  }
  .headline-lead {
    font-family: "Raleway", sans-serif; font-weight: 300; font-size: 34px;
    letter-spacing: 1px; margin-top: 18px;
  }
  .headline-main {
    font-family: "Bebas Neue", sans-serif; font-size: 58px; line-height: 1;
    letter-spacing: -0.5px; margin-top: 2px;
  }
  .headline-intro {
    font-size: 17px; line-height: 1.4; margin: 12px auto 0; width: 640px;
  }
  .accent-rule {
    position: absolute; left: 0; top: 444px; width: 880px; height: 5px; background: var(--red);
  }
  .photo {
    position: absolute; border: 4px solid var(--white);
    box-shadow: 0 1px 4px rgba(0,0,0,.18);
  }
  .photo-cooking { left: 52px; top: 472px; width: 222px; height: 180px;
    background: linear-gradient(135deg, #d8cfc0, #a98c6b 60%, #5f7f9a); }
  .photo-band { left: 280px; top: 472px; width: 150px; height: 180px;
    background: linear-gradient(180deg, #f7f7f7, #f08a7a 55%, #3a3a3a); }
  .photo-backpain { left: 58px; top: 664px; width: 150px; height: 198px;
    background: linear-gradient(160deg, #e9e6dc, #c8c2b0 50%, #3d5fa8); }
  .photo-ball { left: 214px; top: 664px; width: 222px; height: 198px;
    background: linear-gradient(180deg, #f3f1ec 0%, #e5e0d6 45%, #b07a4e 80%, #5aa9c9 100%); }
  .services { position: absolute; left: 456px; top: 472px; width: 400px; list-style: none; }
  .services li, .suggestions li {
    display: flex; align-items: flex-start; gap: 9px;
    font-size: 19px; color: var(--ink); margin-bottom: 8px; line-height: 1.3;
  }
  .bullet { flex: 0 0 16px; margin-top: 4px; }
  .suggestions { position: absolute; left: 466px; top: 648px; width: 400px; }
  .suggestions-title {
    font-family: "Bebas Neue", sans-serif; font-size: 32px; color: var(--teal-deep);
    line-height: 1; margin-bottom: 10px;
  }
  .suggestions-group {
    font-family: "Bebas Neue", sans-serif; font-size: 21px; color: var(--ink);
    margin: 0 0 6px 26px; letter-spacing: .5px; line-height: 1;
  }
  .suggestions ul { list-style: none; margin-left: 6px; }
  .brand { position: absolute; left: 60px; top: 880px; width: 380px; text-align: center; }
  .brand-mark {
    width: 66px; height: 66px; border-radius: 50%; border: 5px solid #c6323c;
    margin: 0 auto 16px;
  }
  .brand-name {
    font-family: "Raleway", sans-serif; font-weight: 600; font-size: 29px;
    letter-spacing: 2.5px; color: var(--grey-text);
  }
  .footer-tab { position: absolute; left: 0; top: 1006px; width: 262px; height: 8px; background: var(--teal); }
  .footer {
    position: absolute; left: 0; top: 1014px; width: 535px; height: 126px;
    background: var(--red); color: var(--white); font-size: 16px;
    display: grid; grid-template-columns: 225px 1fr; grid-auto-rows: 24px;
    padding: 34px 0 0 40px; row-gap: 16px; column-gap: 10px;
  }
  .contact { display: flex; align-items: center; gap: 8px; white-space: nowrap; }
  .social-dot { width: 14px; height: 14px; border-radius: 50%; background: var(--white); flex: 0 0 14px; }
  .card-slot {
    position: absolute; right: 0; bottom: 0; width: 345px; height: 210px; background: var(--white);
  }
</style>
</head>
<body>
<main class="flyer">
  <div class="hero-photo" role="img" aria-label="Trainer and two clients doing push-ups in a sunny Florida park"></div>

  <header class="headline-band">
    <p class="headline-lead">HELPING YOU TO LOSE</p>
    <h1 class="headline-main">WEIGHT, GAIN MUSCLE, AND OWN THE ROOM</h1>
    <p class="headline-intro">Millions of Americans are out of shape and don't know where to start. My name is Marco, owner of Brightwell Fitness, I can show you where to begin.</p>
  </header>
  <div class="accent-rule"></div>

  <div class="photo photo-cooking" role="img" aria-label="Older couple preparing fresh fruit and vegetables in a kitchen"></div>
  <div class="photo photo-band" role="img" aria-label="Smiling woman stretching a resistance band"></div>
  <div class="photo photo-backpain" role="img" aria-label="Man holding his lower back in pain"></div>
  <div class="photo photo-ball" role="img" aria-label="Woman doing crunches with an exercise ball at home"></div>

  <ul class="services">
    <li><svg class="bullet" width="16" height="16" viewBox="0 0 16 16"><circle cx="8" cy="8" r="7" fill="none" stroke="#e8454f" stroke-width="1.5"/><path d="M6.5 4.5 10 8l-3.5 3.5" fill="none" stroke="#e8454f" stroke-width="2"/></svg>Online Fitnes</li>
    <li><svg class="bullet" width="16" height="16" viewBox="0 0 16 16"><circle cx="8" cy="8" r="7" fill="none" stroke="#e8454f" stroke-width="1.5"/><path d="M6.5 4.5 10 8l-3.5 3.5" fill="none" stroke="#e8454f" stroke-width="2"/></svg>In Your Home Fitnes</li>
    <li><svg class="bullet" width="16" height="16" viewBox="0 0 16 16"><circle cx="8" cy="8" r="7" fill="none" stroke="#e8454f" stroke-width="1.5"/><path d="M6.5 4.5 10 8l-3.5 3.5" fill="none" stroke="#e8454f" stroke-width="2"/></svg>Park and Beaches Fitnes</li>
    <li><svg class="bullet" width="16" height="16" viewBox="0 0 16 16"><circle cx="8" cy="8" r="7" fill="none" stroke="#e8454f" stroke-width="1.5"/><path d="M6.5 4.5 10 8l-3.5 3.5" fill="none" stroke="#e8454f" stroke-width="2"/></svg>Bride, Groom ,and Bridal<br>Party Fitnes</li>
  </ul>

  <section class="suggestions">
    <h2 class="suggestions-title">HEALTHY LIVING SUGGESTIONS</h2>
    <h3 class="suggestions-group">NUTRITION</h3>
    <ul>
      <li><svg class="bullet" width="16" height="16" viewBox="0 0 16 16"><circle cx="8" cy="8" r="7" fill="none" stroke="#e8454f" stroke-width="1.5"/><path d="M6.5 4.5 10 8l-3.5 3.5" fill="none" stroke="#e8454f" stroke-width="2"/></svg>Prepared Meals</li>
      <li><svg class="bullet" width="16" height="16" viewBox="0 0 16 16"><circle cx="8" cy="8" r="7" fill="none" stroke="#e8454f" stroke-width="1.5"/><path d="M6.5 4.5 10 8l-3.5 3.5" fill="none" stroke="#e8454f" stroke-width="2"/></svg>Grocery/Markets</li>
      <li><svg class="bullet" width="16" height="16" viewBox="0 0 16 16"><circle cx="8" cy="8" r="7" fill="none" stroke="#e8454f" stroke-width="1.5"/><path d="M6.5 4.5 10 8l-3.5 3.5" fill="none" stroke="#e8454f" stroke-width="2"/></svg>On the Go</li>
    </ul>
    <h3 class="suggestions-group">EQUIPMENT</h3>
    <ul>
      <li><svg class="bullet" width="16" height="16" viewBox="0 0 16 16"><circle cx="8" cy="8" r="7" fill="none" stroke="#e8454f" stroke-width="1.5"/><path d="M6.5 4.5 10 8l-3.5 3.5" fill="none" stroke="#e8454f" stroke-width="2"/></svg>Stretching/Mobility</li>
      <li><svg class="bullet" width="16" height="16" viewBox="0 0 16 16"><circle cx="8" cy="8" r="7" fill="none" stroke="#e8454f" stroke-width="1.5"/><path d="M6.5 4.5 10 8l-3.5 3.5" fill="none" stroke="#e8454f" stroke-width="2"/></svg>Footwear</li>
    </ul>
  </section>

  <div class="brand">
    <div class="brand-mark"></div>
    <p class="brand-name">BRIGHTWELL FITNESS</p>
  </div>

  <div class="footer-tab"></div>
  <footer class="footer">
    <span class="contact"><svg width="14" height="14" viewBox="0 0 16 16"><path d="M4 1h3l1 4-2 1.5a9 9 0 0 0 3.5 3.5L11 8l4 1v3c0 1.5-1 3-3 3A11 11 0 0 1 1 4c0-2 1.5-3 3-3z" fill="#fff"/></svg>555 214 7730</span>
    <span class="contact"><svg width="15" height="12" viewBox="0 0 16 12"><rect x="1" y="1" width="14" height="10" rx="1" fill="none" stroke="#fff" stroke-width="1.6"/><path d="M1.5 1.5 8 7l6.5-5.5" fill="none" stroke="#fff" stroke-width="1.6"/></svg>hello@brightwellfitness.com</span>
    <span class="contact"><svg width="14" height="14" viewBox="0 0 16 16"><circle cx="8" cy="8" r="6.5" fill="none" stroke="#fff" stroke-width="1.5"/><path d="M1.5 8h13M8 1.5c-3 3.5-3 9.5 0 13M8 1.5c3 3.5 3 9.5 0 13" fill="none" stroke="#fff" stroke-width="1.2"/></svg>www.brightwellfitness.com</span>
    <span class="contact"><span class="social-dot"></span>@brightwellfitness</span>
  </footer>

  <div class="card-slot"></div>
</main>
</body>
</html>
```